Business Card Design Project

We need a redesign of our business card.
We are a Consulting Property Developer called The Kestrel Group
Updates

Thank you all for submissions. Just waiting on managment to decide.

Thank you,

Dorinda

Industry/Entity Type

Business

Requirements
Must have
• we like having the KG a focus in the back ground or on the side
Kestrel is our company colour

the wording - property development
and - premium accommodation

our website www.kestrelgroup-example.com.au

persons name
title

p: 1300 482917 f: 1300 482915 m: 0417593824
PO Box 5817, Brindlevale Qld 4178
e: admin@kestrelgroup-example.com.au

```html
<!DOCTYPE html>
<html lang="en">
<head>
<meta charset="utf-8">
<title>The Kestrel Group – Business Card</title>
<link href="https://fonts.googleapis.com/css2?family=Bilbo+Swash+Caps&display=swap" rel="stylesheet">
<style>
  :root {
    --card-light: #f7f8f9;
    --card-mid: #e4e6e8;
    --card-edge: #d9dbde;
    --band-dark: #9e9a9c;
    --band-mid: #c9c6c8;
    --band-light: #ecebec;
    --ink: #6a1c1c;
    --ink-faint: rgba(106, 28, 28, 0.07);
    --glow: rgba(220, 120, 130, 0.75);
  }
  html, body {
    margin: 0;
    padding: 0;
    width: 1200px;
    height: 903px;
    overflow: hidden;
    background: #ffffff;
  }
  .card {
    position: relative;
    width: 1200px;
    height: 903px;
    overflow: hidden;
    background: radial-gradient(ellipse 60% 55% at 48% 40%, var(--card-light) 0%, var(--card-mid) 70%, var(--card-edge) 100%);
    font-family: "Bilbo Swash Caps", cursive;
    color: var(--ink);
  }
  .card__ornament {
    position: absolute;
    left: 300px;
    top: 110px;
    width: 560px;
    height: 520px;
    border-radius: 50%;
    background: radial-gradient(ellipse at center, rgba(255,255,255,0.85) 0%, rgba(255,255,255,0.35) 50%, rgba(255,255,255,0) 72%);
  }
  .monogram {
    position: absolute;
    left: 0;
    width: 1200px;
    top: 170px;
    margin: 0;
    text-align: center;
    font-size: 300px;
    line-height: 1;
    color: var(--ink-faint);
  }
  .card__band {
    position: absolute;
    left: 0;
    top: 0;
    width: 1200px;
    height: 903px;
  }
  .text {
    position: absolute;
    margin: 0;
    line-height: 1;
    text-shadow: 0 0 6px var(--glow), 0 0 12px var(--glow);
    white-space: nowrap;
  }
  .person {
    left: 14px;
    top: 80px;
    width: 260px;
    text-align: center;
    font-size: 48px;
  }
  .person__title {
    display: block;
    margin-top: 4px;
    font-size: 44px;
  }
  .contact {
    right: 48px;
    top: 82px;
    text-align: right;
    font-size: 44px;
  }
  .contact span { display: block; margin-bottom: 10px; }
  .tagline {
    left: 0;
    width: 1200px;
    top: 500px;
    text-align: center;
    font-size: 36px;
  }
  .address {
    left: 10px;
    top: 698px;
    font-size: 46px;
  }
  .address span { display: block; margin-bottom: 6px; }
  .address__street { font-size: 48px; }
  .address__web { font-size: 44px; }
</style>
</head>
<body>
  <div class="card">
    <div class="card__ornament" role="img" aria-label="Soft white flourish ornament in the centre of the card"></div>
    <p class="monogram" aria-hidden="true">KG</p>

    <svg class="card__band" viewBox="0 0 1200 903" aria-hidden="true">
      <defs>
        <linearGradient id="bandFill" x1="0" y1="0" x2="1" y2="0">
          <stop offset="0" stop-color="var(--band-dark)"/>
          <stop offset="0.35" stop-color="var(--band-mid)"/>
          <stop offset="0.55" stop-color="var(--band-light)"/>
          <stop offset="0.75" stop-color="var(--band-mid)"/>
          <stop offset="1" stop-color="var(--band-dark)"/>
        </linearGradient>
      </defs>
      <path d="M0 606 C 260 590, 520 660, 760 725 C 960 780, 1100 790, 1200 770 L 1200 903 L 0 903 Z" fill="url(#bandFill)"/>
      <path d="M0 606 C 260 590, 520 660, 760 725 C 960 780, 1100 790, 1200 770" fill="none" stroke="#ffffff" stroke-opacity="0.6" stroke-width="2"/>
    </svg>

    <p class="text person">
      <span class="person__name">Persons Name</span>
      <span class="person__title">title</span>
    </p>

    <p class="text contact">
      <span class="contact__phone">Phone: 1300 482917</span>
      <span class="contact__fax">Fax: 1300 482915</span>
      <span class="contact__mobile">Mobile: 0417593824</span>
    </p>

    <p class="text tagline">property development &middot; premium accommodation</p>

    <p class="text address">
      <span class="address__street">PO Box 5817, Brindlevale Qld 4178</span>
      <span class="address__email">email: admin@kestrelgroup-example.com.au</span>
      <span class="address__web">www.kestrelgroup-example.com.au</span>
    </p>
  </div>
</body>
</html>
```